Design a Flyer for Wedding and Party consultants

I would like to create a Wedding, Bridal, Party flyer which telling a prospective client what we do and what we offer.
The wording in the sample that I upload are wrong. Please use a better English :)

```html
<!DOCTYPE html>
<html lang="en">
<head>
<meta charset="utf-8">
<title>Evermore Events – Wedding &amp; Party Brochure</title>
<link rel="stylesheet" href="https://fonts.googleapis.com/css2?family=Cormorant+Garamond:ital,wght@0,600;1,500;1,600&family=Roboto+Condensed:wght@400;700&display=swap">
<style>
  :root {
    --backdrop: #a9c6c3;
    --paper: #ffffff;
    --salmon: #e9767b;
    --salmon-light: #f4a7aa;
    --blush: #f7c9d2;
    --rose: #ec7598;
    --crimson: #d3124c;
    --crimson-deep: #a80c3a;
    --maroon: #7a0f2e;
    --gold: #f4c84a;
    --ink: #3a1a24;
  }
  * { box-sizing: border-box; margin: 0; padding: 0; }
  html, body {
    width: 1200px; height: 1200px; overflow: hidden;
    background: var(--backdrop);
  }
  .brochure {
    position: absolute; left: 60px; top: 150px;
    width: 1080px; height: 900px;
    background: var(--paper);
    box-shadow: 0 12px 30px rgba(0,0,0,.18);
    overflow: hidden;
  }
  .brochure__art { position: absolute; inset: 0; width: 1080px; height: 900px; }
  .fold { position: absolute; top: 0; width: 1px; height: 900px; background: rgba(0,0,0,.06); }
  .fold--first { left: 360px; }
  .fold--second { left: 720px; }

  .heading {
    font-family: "Roboto Condensed", sans-serif;
    font-weight: 700; text-transform: uppercase; letter-spacing: .3px;
  }
  .script {
    font-family: "Cormorant Garamond", serif;
    font-style: italic; font-weight: 600;
  }

  /* Left panel */
  .packages { position: absolute; left: 36px; top: 46px; width: 300px; }
  .packages__title { color: var(--paper); font-size: 22px; margin-bottom: 16px; }
  .packages__list { list-style: none; }
  .packages__item {
    position: relative; padding-left: 22px; margin-bottom: 5px;
    font-family: "Roboto Condensed", sans-serif; font-weight: 700;
    font-size: 16px; line-height: 1.12; text-transform: uppercase;
    color: var(--maroon);
  }
  .packages__heart { position: absolute; left: 0; top: 2px; width: 15px; height: 14px; }
  .promise {
    position: absolute; left: 34px; top: 640px; width: 270px;
    color: var(--maroon); font-size: 16.5px; line-height: 1.22;
  }
  .promise + .promise { top: 790px; }

  /* Middle panel */
  .welcome {
    position: absolute; left: 392px; top: 330px; width: 235px;
    color: var(--maroon); font-size: 17px; line-height: 1.3;
  }
  .welcome p + p { margin-top: 16px; }
  .brand {
    display: flex; align-items: center; gap: 8px;
    font-family: "Roboto Condensed", sans-serif; font-weight: 700;
    text-transform: uppercase; color: var(--crimson); letter-spacing: 1px;
  }
  .brand__dot { width: 14px; height: 14px; border-radius: 50%; background: var(--crimson); flex: none; }
  .brand--center { position: absolute; left: 400px; top: 690px; font-size: 26px; }
  .contact {
    position: absolute; left: 420px; top: 742px; width: 220px;
    font-family: "Roboto Condensed", sans-serif; font-size: 13px; line-height: 1.35;
    color: var(--ink); text-align: center;
  }

  /* Right panel */
  .brand--cover { position: absolute; left: 800px; top: 90px; font-size: 28px; }
  .tagline {
    position: absolute; right: 22px; top: 370px; width: 120px;
    color: var(--paper); font-size: 18px; line-height: 1.15; text-align: right;
  }
  .services { position: absolute; right: 24px; top: 690px; text-align: right; }
  .services__title { color: var(--gold); font-size: 21px; margin-bottom: 8px; }
  .services__list { list-style: none; }
  .services__item {
    font-family: "Roboto Condensed", sans-serif; font-weight: 700;
    font-size: 15px; line-height: 1.25; text-transform: uppercase; color: var(--paper);
  }
</style>
</head>
<body>
<main class="brochure">
  <svg class="brochure__art" viewBox="0 0 1080 900" xmlns="http://www.w3.org/2000/svg">
    <defs>
      <linearGradient id="salmonWash" x1="0" y1="0" x2="0" y2="1">
        <stop offset="0" stop-color="#e86a71"/>
        <stop offset="1" stop-color="#f4a7aa"/>
      </linearGradient>
      <linearGradient id="blushWash" x1="0" y1="0" x2="1" y2="1">
        <stop offset="0" stop-color="#f7c9d2"/>
        <stop offset="1" stop-color="#fbe6ec"/>
      </linearGradient>
      <radialGradient id="bouquetWash" cx=".65" cy=".4" r=".7">
        <stop offset="0" stop-color="#f6c7b8"/>
        <stop offset=".45" stop-color="#f199ad"/>
        <stop offset="1" stop-color="#e9668d"/>
      </radialGradient>
      <linearGradient id="crimsonWash" x1="1" y1="0" x2="0" y2="1">
        <stop offset="0" stop-color="#c80f45"/>
        <stop offset=".4" stop-color="#d3124c"/>
        <stop offset="1" stop-color="#dc2457"/>
      </linearGradient>
    </defs>

    <!-- left panel -->
    <rect x="0" y="0" width="360" height="900" fill="#ffffff"/>
    <path d="M0 0 H360 V600 C260 640 120 600 0 650 Z" fill="url(#salmonWash)"
          role="img" aria-label="Soft pink cosmos flowers behind the package list"/>

    <!-- middle panel -->
    <rect x="360" y="0" width="360" height="900" fill="url(#blushWash)"/>

    <!-- right panel -->
    <rect x="720" y="0" width="360" height="900" fill="#ffffff"/>
    <path d="M720 900 V430 C820 370 950 320 1080 300 V900 Z" fill="url(#crimsonWash)"
          role="img" aria-label="Red gerbera flower photographed on the crimson band"/>

    <!-- central circle -->
    <circle cx="560" cy="430" r="352" fill="#ffffff" opacity=".92"/>
    <circle cx="560" cy="430" r="330" fill="url(#bouquetWash)"
            role="img" aria-label="Bridal bouquet of cream roses and pink flowers"/>
  </svg>

  <div class="fold fold--first"></div>
  <div class="fold fold--second"></div>

  <!-- Left panel -->
  <section class="packages">
    <h2 class="packages__title heading">Our Wedding Packages</h2>
    <ul class="packages__list">
      <li class="packages__item"><svg class="packages__heart" viewBox="0 0 16 14"><path d="M8 14 L1.5 7.2 A3.9 3.9 0 0 1 8 2.3 A3.9 3.9 0 0 1 14.5 7.2 Z" fill="#7a0f2e"/></svg>Standard Stage Decoration</li>
      <li class="packages__item"><svg class="packages__heart" viewBox="0 0 16 14"><path d="M8 14 L1.5 7.2 A3.9 3.9 0 0 1 8 2.3 A3.9 3.9 0 0 1 14.5 7.2 Z" fill="#7a0f2e"/></svg>Welcome Board &amp; Entrance Gate</li>
      <li class="packages__item"><svg class="packages__heart" viewBox="0 0 16 14"><path d="M8 14 L1.5 7.2 A3.9 3.9 0 0 1 8 2.3 A3.9 3.9 0 0 1 14.5 7.2 Z" fill="#7a0f2e"/></svg>Bridal Suite Styling</li>
      <li class="packages__item"><svg class="packages__heart" viewBox="0 0 16 14"><path d="M8 14 L1.5 7.2 A3.9 3.9 0 0 1 8 2.3 A3.9 3.9 0 0 1 14.5 7.2 Z" fill="#7a0f2e"/></svg>Aisle Flower Arrangements</li>
      <li class="packages__item"><svg class="packages__heart" viewBox="0 0 16 14"><path d="M8 14 L1.5 7.2 A3.9 3.9 0 0 1 8 2.3 A3.9 3.9 0 0 1 14.5 7.2 Z" fill="#7a0f2e"/></svg>Wedding Car Decoration</li>
      <li class="packages__item"><svg class="packages__heart" viewBox="0 0 16 14"><path d="M8 14 L1.5 7.2 A3.9 3.9 0 0 1 8 2.3 A3.9 3.9 0 0 1 14.5 7.2 Z" fill="#7a0f2e"/></svg>Bridal Hand Bouquet</li>
      <li class="packages__item"><svg class="packages__heart" viewBox="0 0 16 14"><path d="M8 14 L1.5 7.2 A3.9 3.9 0 0 1 8 2.3 A3.9 3.9 0 0 1 14.5 7.2 Z" fill="#7a0f2e"/></svg>Flower Petals</li>
      <li class="packages__item"><svg class="packages__heart" viewBox="0 0 16 14"><path d="M8 14 L1.5 7.2 A3.9 3.9 0 0 1 8 2.3 A3.9 3.9 0 0 1 14.5 7.2 Z" fill="#7a0f2e"/></svg>Groom's Corsage</li>
      <li class="packages__item"><svg class="packages__heart" viewBox="0 0 16 14"><path d="M8 14 L1.5 7.2 A3.9 3.9 0 0 1 8 2.3 A3.9 3.9 0 0 1 14.5 7.2 Z" fill="#7a0f2e"/></svg>Family Corsages</li>
      <li class="packages__item"><svg class="packages__heart" viewBox="0 0 16 14"><path d="M8 14 L1.5 7.2 A3.9 3.9 0 0 1 8 2.3 A3.9 3.9 0 0 1 14.5 7.2 Z" fill="#7a0f2e"/></svg>Ribbons for VIP Chairs</li>
      <li class="packages__item"><svg class="packages__heart" viewBox="0 0 16 14"><path d="M8 14 L1.5 7.2 A3.9 3.9 0 0 1 8 2.3 A3.9 3.9 0 0 1 14.5 7.2 Z" fill="#7a0f2e"/></svg>Red Carpet</li>
      <li class="packages__item"><svg class="packages__heart" viewBox="0 0 16 14"><path d="M8 14 L1.5 7.2 A3.9 3.9 0 0 1 8 2.3 A3.9 3.9 0 0 1 14.5 7.2 Z" fill="#7a0f2e"/></svg>Wedding Keepsake Bookmarks</li>
      <li class="packages__item"><svg class="packages__heart" viewBox="0 0 16 14"><path d="M8 14 L1.5 7.2 A3.9 3.9 0 0 1 8 2.3 A3.9 3.9 0 0 1 14.5 7.2 Z" fill="#7a0f2e"/></svg>Angpau Box (Red Envelope Box)</li>
    </ul>
  </section>

  <p class="promise script">Your complete satisfaction is our priority – in our expertise, our designs, our service and our prices. The designer who creates your flower arrangements will also deliver and set them up at your venue.</p>
  <p class="promise script">Fresh or artificial flowers are available on request. For more information, please call us on +61 400 555 218.</p>

  <!-- Middle panel -->
  <div class="welcome script">
    <p>Throw the perfect celebration with our creative designs, quality materials and stylish, up-to-date works of art.</p>
    <p>Whether it's a wedding ceremony or a first birthday party, find the theme that makes your day extra special – and let us make the planning simple!</p>
  </div>

  <div class="brand brand--center"><span class="brand__dot"></span>Evermore Events</div>
  <address class="contact" style="font-style:normal">
    12345 Name of Street, Name of Town<br>
    Name of City, Australia 678910<br>
    +61 400 555 218<br>
    hello@evermore-events.com
  </address>

  <!-- Right panel -->
  <div class="brand brand--cover"><span class="brand__dot"></span>Evermore Events</div>

  <p class="tagline script">Every Occasion You Celebrate Is Special to Us</p>

  <section class="services">
    <h2 class="services__title heading">Our Services</h2>
    <ul class="services__list">
      <li class="services__item">Weddings</li>
      <li class="services__item">Bridal Showers</li>
      <li class="services__item">Baby Showers</li>
      <li class="services__item">Sweet Seventeen</li>
      <li class="services__item">Birthdays</li>
      <li class="services__item">Kids' Birthdays</li>
      <li class="services__item">All Occasions</li>
    </ul>
  </section>
</main>
</body>
</html>
```